Rodeo Sponsor booklet

I am needing a multi page handout made for potential sponsors for our Pell Creek Stampede. I have attached our previous one and our 2025 poster that we would like it to flow similarly. You will see on the "example of 2025" the markup we would like changed and of course new front cover etc.
These are the following uploads
This is the new information that is needed on the new 2025 brochure with changes that I would like made. it can have what ever look and feel I was just playing around. nothing about it needs to be similar to this but all information does need to be in the document
The rest are photos we like and you can use which ever I just like the look and feel of the 2024 one so want that same feeling!

```html
<!DOCTYPE html>
<html lang="en">
<head>
<meta charset="utf-8">
<title>Pell Creek Stampede – Sponsor Booklet</title>
<link href="https://fonts.googleapis.com/css2?family=Oswald:wght@500;700&family=Josefin+Slab:wght@400;600&family=Bebas+Neue&display=swap" rel="stylesheet">
<style>
:root{
  --backdrop:#a6a6a6;
  --cover-brown:#2b1a17;
  --page-brown:#3b2823;
  --letter-frame:#24150f;
  --paper:#ffffff;
  --ink:#2b1a17;
  --cream:#ffffff;
  --muted:#e6dcd6;
}
*{margin:0;padding:0;box-sizing:border-box}
html,body{width:857px;height:1200px;overflow:hidden;background:var(--backdrop)}
.canvas{position:relative;width:857px;height:1200px}
.page{position:absolute;overflow:hidden}

/* cover */
.cover{left:244px;top:69px;width:369px;height:522px;background:var(--cover-brown)}
.cover__photo{position:absolute;left:0;top:0;width:100%;height:340px;
  background:linear-gradient(180deg,#c9cdd3 0%,#9a9ea4 35%,#5d4a44 70%,var(--cover-brown) 100%)}
.event-name{position:absolute;left:0;right:0;top:282px;text-align:center;
  font-family:"Oswald",sans-serif;font-weight:700;font-size:44px;line-height:50px;
  color:var(--cream);letter-spacing:.5px}
.cover__date{position:absolute;left:0;right:0;top:400px;text-align:center;
  font-family:"Oswald",sans-serif;font-weight:500;font-size:30px;color:var(--cream)}
.cover__host{position:absolute;left:0;right:0;top:440px;text-align:center;
  font-family:"Josefin Slab",serif;font-weight:400;font-size:28px;color:var(--cream)}
.cover__motto{position:absolute;left:0;right:0;top:478px;text-align:center;
  font-family:"Josefin Slab",serif;font-size:12.5px;color:var(--cream)}

/* letter */
.letter{left:41px;top:620px;width:371px;height:523px;background:var(--letter-frame)}
.letter__sheet{position:absolute;left:14px;top:15px;width:342px;height:494px;background:var(--paper);
  padding:30px 15px 10px 16px;font-family:"Josefin Slab",serif;font-size:7px;line-height:9px;color:#222;text-align:justify}
.letter__sheet p{margin-bottom:8px}

/* levels */
.levels{left:446px;top:620px;width:370px;height:523px;background:var(--page-brown)}
.levels__photo{position:absolute;inset:0;
  background:radial-gradient(ellipse at 50% 55%,#5a4139 0%,#3b2823 60%,#2f1f1b 100%)}
.levels__title{position:absolute;left:0;right:0;top:24px;text-align:center;
  font-family:"Bebas Neue",sans-serif;font-weight:400;font-size:30px;color:var(--cream);letter-spacing:.2px}
.tier{position:absolute;width:165px}
.tier__head{display:flex;height:32px}
.tier__name{width:92px;background:var(--paper);color:var(--ink);font-family:"Josefin Slab",serif;
  font-size:12.5px;line-height:14px;padding:2px 0 0 26px}
.tier__price{width:71px;background:#2a1b17;color:var(--cream);font-family:"Josefin Slab",serif;
  font-size:20px;line-height:32px;text-align:center}
.tier__perks{list-style:none;margin-top:15px;padding-left:26px;width:138px;font-family:"Josefin Slab",serif;
  font-size:7px;line-height:8.9px;color:var(--muted)}
.tier--right .tier__name{width:77px;padding-left:12px}
.tier--right .tier__perks{padding-left:9px;width:138px}
.tier--wide{width:340px}
.tier--wide .tier__perks{width:300px}
</style>
</head>
<body>
<div class="canvas">

  <section class="page cover">
    <div class="cover__photo" role="img" aria-label="Photo of a rider in a helmet on a dark horse clearing a show jump under a cloudy sky"></div>
    <h1 class="event-name">PELL CREEK<br>STAMPEDE</h1>
    <div class="cover__date">1,2,3 AUG 2025</div>
    <div class="cover__host">Pell Creek First Nation</div>
    <div class="cover__motto">"Ride hard, shoot straight, and speak the truth."</div>
  </section>

  <section class="page letter">
    <div class="letter__sheet">
      <p>Dear Valued Sponsor,</p>
      <p>I hope this letter finds you well.</p>
      <p>As we reflect on the incredible success of the 2024 Pell Creek Stampede, we are filled with gratitude and excitement. Each year, our event continues to grow, and thanks to the support of our sponsors, we are proud to uphold a 36-year tradition that brings together cowboys, cowgirls, and rodeo fans from across the region.</p>
      <p>We are thrilled to announce that 2025 will be a landmark year for the Pell Creek Stampede! Not only are we planning another action-packed rodeo season, but we are also working on the construction of our new rodeo arena, set to open in 2026. This state-of-the-art facility, located just north of our community, will feature top-tier rodeo equipment, new buildings, offices, announcer booths, and more-enhancing the experience for both contestants and spectators.</p>
      <p>The 2025 Pell Creek Stampede will continue its tradition of two thrilling, one-day events, where contestants have a chance to win a custom buckle each day.<br>Additionally, we are excited to introduce a custom Pell Drum for the Average winner, adding a unique and meaningful prize to our event.</p>
      <p>This year, we're bringing even more excitement with the return of the Mini Wild Pony Race, along with fantastic entertainment featuring Dusty Spur. Our substantial payout remains a major draw, ensuring a high level of competition and attracting a larger and more diverse group of skilled participants.</p>
      <p>Your sponsorship is more than just a contribution-it's an investment in the future of rodeo and a commitment to preserving an important community tradition. Funds raised will support critical needs, including ground upgrades, rodeo stock, event payouts, prizes, and essential supplies.</p>
      <p>Enclosed, you'll find our 2025 sponsorship levels for your consideration. This year, we've made contributions even more convenient with multiple payment options, including Electronic Funds Transfer (EFT), e-Transfer, credit, debit, or cheque. All payments must be sent to 4410 Ridge Rd, Aldercreek, BC V0C 2K4. Please complete one of the attached forms at your earliest convenience.</p>
      <p>If you have any questions or need further details, please don't hesitate to reach out. Together, let's make the 2025 Pell Creek Stampede an unforgettable event that continues to honor the rich heritage and spirit of our community.</p>
      <p>We look forward to seeing you there!</p>
      <p>Sincerely,<br>Marla Keene<br>Pell Creek Stampede Manager</p>
      <p>"A rodeo is not just an event; it's a way of life. It's where courage meets determination, where tradition meets competition, and where a community comes together. Thank you for being part of our rodeo family."</p>
    </div>
  </section>

  <section class="page levels">
    <div class="levels__photo" role="img" aria-label="Faded photo of a young rider in a helmet sitting on a chestnut horse in an arena"></div>
    <h2 class="levels__title">BASE SPONSORSHIP LEVELS</h2>

    <div class="tier" style="left:0;top:87px">
      <div class="tier__head"><div class="tier__name">Bronze<br>Supporter</div><div class="tier__price">$1500</div></div>
      <ul class="tier__perks" style="width:138px">
        <li>Company name listed in the event program.</li>
        <li>Social media mention on all rodeo related pages.</li>
        <li>Small logo display on the event's main digital screen.</li>
        <li>4 Single Day Passes to the rodeo.</li>
      </ul>
    </div>

    <div class="tier tier--right" style="left:208px;top:87px">
      <div class="tier__head"><div class="tier__name">Silver<br>Supporter</div><div class="tier__price">$3000</div></div>
      <ul class="tier__perks">
        <li>Includes all Bronze Supporter benefits.</li>
        <li>Company logo on the event website.</li>
        <li>Company banner displayed at the event (provided by the rodeo).</li>
        <li>8 Single Day Passes to the rodeo.</li>
      </ul>
    </div>

    <div class="tier" style="left:0;top:244px">
      <div class="tier__head"><div class="tier__name">Gold<br>Supporter</div><div class="tier__price">$5000</div></div>
      <ul class="tier__perks">
        <li>Includes all Silver Sponsor benefits.</li>
        <li>Medium-sized banner at the event (provided by the rodeo).</li>
        <li>6 Weekend Passes to the rodeo.</li>
      </ul>
    </div>

    <div class="tier tier--right" style="left:208px;top:244px">
      <div class="tier__head"><div class="tier__name">Platinum<br>Supporter</div><div class="tier__price">$6500</div></div>
      <ul class="tier__perks">
        <li>Includes all Bronze Supporter benefits.</li>
        <li>Company logo on the event website.</li>
        <li>Company banner displayed at the event (provided by the rodeo).</li>
        <li>10 weekend passes with VIP seating to the rodeo</li>
      </ul>
    </div>

    <div class="tier tier--wide" style="left:0;top:384px">
      <div class="tier__head"><div class="tier__name">Diamond<br>Supporter</div><div class="tier__price">$8500</div></div>
      <ul class="tier__perks">
        <li>Includes all Platinum Contributor benefits.</li>
        <li>Large banner in a prime location at the event (provided by the rodeo).</li>
        <li>Exclusive 2 VIP parking spots.</li>
        <li>12 Weekend VIP Passes to the Rodeo.</li>
        <li>Option to provide short Commercial for your company.</li>
        <li>Option to provide short Commercial for your company.</li>
        <li>A banner on one of the 6 chutes or main gates used in the arena.</li>
      </ul>
    </div>
  </section>

</div>
</body>
</html>
```